Business Card for Jewelry Business

We need a new namecard design for a jewelry company based in Bangkok, Thailand. We have a new website recently and want the new namecard to reflect our new modern image. I have uploaded our old namecard to show you the information that needs to be on the namecard. Pls check our website www.qelburn.com for the new color scheme to help design the new namecard.

```html
<!DOCTYPE html>
<html lang="en">
<head>
<meta charset="utf-8">
<title>Qelburn Jewelry – Business Card</title>
<link rel="stylesheet" href="https://fonts.googleapis.com/css2?family=Cinzel:wght@400;600&family=Questrial&display=swap">
<style>
  :root {
    --backdrop: #2f4360;
    --card-white: #ffffff;
    --teal: #63c3cb;
    --ink: #1c1c1c;
    --ink-soft: #333333;
    --on-teal: #ffffff;
  }
  * { margin: 0; padding: 0; box-sizing: border-box; }
  html, body { width: 1200px; height: 982px; overflow: hidden; }
  body { background: var(--backdrop); position: relative; font-family: "Questrial", sans-serif; }

  .card {
    position: absolute;
    left: 297px;
    width: 573px;
    height: 327px;
    box-shadow: 0 6px 18px rgba(0,0,0,0.35);
  }
  .card--front { top: 136px; background: var(--card-white); color: var(--ink); }
  .card--back { top: 509px; background: var(--teal); color: var(--on-teal); }

  .accent-square {
    position: absolute; top: 0; right: 38px;
    width: 38px; height: 48px; background: var(--teal);
  }

  .brand {
    position: absolute;
    font-family: "Cinzel", serif;
    font-weight: 400;
    letter-spacing: 1px;
    white-space: nowrap;
  }
  .card--front .brand { left: 32px; top: 56px; font-size: 21px; color: var(--teal); }
  .card--back .brand { left: 0; right: 0; top: 140px; text-align: center; font-size: 30px; color: var(--on-teal); }

  .person-name {
    position: absolute; left: 27px; top: 184px;
    font-family: "Cinzel", serif; font-weight: 400;
    font-size: 28px; letter-spacing: 1px; line-height: 1;
  }
  .person-title {
    position: absolute; left: 28px; top: 215px;
    font-size: 8.5px; letter-spacing: 1.6px; color: var(--ink-soft);
  }
  .company {
    position: absolute; left: 28px; top: 239px;
    font-family: "Cinzel", serif; font-weight: 600;
    font-size: 13.5px; letter-spacing: 0.6px;
  }
  .address {
    position: absolute; left: 28px; top: 262px;
    font-size: 10.8px; line-height: 14.5px; font-style: normal;
  }
  .contact {
    position: absolute; left: 382px; top: 218px;
    font-size: 10.6px; line-height: 14.8px; list-style: none;
  }
  .contact .label { display: inline-block; width: 18px; }
  .contact .email-main { font-size: 13px; }
  .contact .indent { padding-left: 18px; }

  .website {
    position: absolute; left: 0; right: 0; bottom: 16px;
    text-align: center; font-size: 13px; letter-spacing: 0.5px;
  }
</style>
</head>
<body>
  <section class="card card--front">
    <div class="accent-square"></div>
    <div class="brand">Qelburn Jewelry</div>

    <h1 class="person-name">NAREE SITTIPONG</h1>
    <p class="person-title">SALES &amp; PRODUCT DEVELOPMENT MANAGER</p>
    <p class="company">QELBURN JEWELRY CO. LTD</p>
    <address class="address">
      218 Moo 7 Sukhaprachan Road,<br>
      Export Processing Zone 2, Ban Klong Industrial Estate<br>
      Ban Klong Bangkok 10590 Thailand.
    </address>

    <ul class="contact">
      <li><span class="label">T:</span>+662-415-2270</li>
      <li><span class="label">Fx:</span>+662-508-3391</li>
      <li><span class="label">Fb:</span>Qelburn Jewelry</li>
      <li><span class="label">Ig:</span>@QelburnJwl</li>
      <li><span class="label">E:</span><span class="email-main">naree@qelburn.com</span></li>
      <li class="indent">info@qelburn.com</li>
    </ul>
  </section>

  <section class="card card--back">
    <div class="brand">Qelburn Jewelry</div>
    <p class="website">www.qelburn.net</p>
  </section>
</body>
</html>
```